Sale of South Sea and Tahitian Pearl Jewellery, online business

I need a business card designed for my website business. We sell South Sea and Tahitian Pearl Jewellery. The colour theme for the website is black and white and would like to carry this through to business cards. Our brand is very elegant and stylish, would like sketch picture of women or fashion involving pearls if not the sketched picture then have the card very plan. below are pictures of the ideas I like and also the logo and writing that is used on my jewellery boxes.
Font is English Hand DB

Target Market(s)

30 and over women in the high end of the market

Industry/Entity Type

Business

Contact Information for Business Card

Business name - Varno Gems( front of card)
Back of card -Details
Corinne Mabbutt
Gemmologist FGAA
email: corinne@varnogems.com.au
website: varnogems.com.au
mob: +61 427 806 193
Perth Australia

Varno Orbix PTY T/AS Varno Gems
ABN 72 384 516 907

Colors
1b1b1b
ffffff
85cae6

Requirements
Must have
• Black and white colour preferably black card with white writing and picture.
• The Same writing as logo and writing on box packaging, attached a file with writing.
• Business name on one side of the card and all other details on the other side.
• Can have tiny hints of the tiffany blue colour.
• Font: English Hand DB
Nice to have
• I really like the idea of having a sketch of a stylish or elegent lady wearing pearls or a sketch of a pearl, if not the sketch a really plain and simple card.
Should not have
• busy patterns.

```html
<!DOCTYPE html>
<html lang="en">
<head>
<meta charset="utf-8">
<title>Varno Gems – Business Cards</title>
<link rel="stylesheet" href="https://fonts.googleapis.com/css2?family=Montserrat:wght@300;400;600&display=swap">
<style>
  :root {
    --ink: #1b1b1b;
    --black: #0a0a0a;
    --paper: #ffffff;
    --stage: #e9e6e1;
    --muted: #3a3a3a;
    --soft-white: #e8e8e8;
  }
  html, body {
    margin: 0;
    padding: 0;
    width: 1200px;
    height: 913px;
    overflow: hidden;
    background: var(--stage);
    font-family: "Montserrat", sans-serif;
  }
  .canvas {
    position: relative;
    width: 1200px;
    height: 913px;
  }
  .card {
    position: absolute;
    top: 302px;
    width: 540px;
    height: 309px;
    border-radius: 16px;
    overflow: hidden;
    box-shadow: 0 10px 26px rgba(0,0,0,0.22);
  }
  .card svg { position: absolute; inset: 0; }
  .card--details { left: 40px; background: var(--paper); }
  .card--brand { left: 620px; background: var(--black); }

  .contact {
    position: absolute;
    top: 30px;
    right: 34px;
    text-align: right;
    color: var(--ink);
  }
  .contact__name {
    font-weight: 600;
    font-size: 21px;
    margin: 0;
    letter-spacing: 0.2px;
  }
  .contact__title {
    font-weight: 400;
    font-size: 13px;
    margin: 2px 0 0;
    color: var(--muted);
  }
  .contact__city {
    font-size: 13px;
    margin: 16px 0 0;
    color: var(--muted);
  }
  .contact__list {
    list-style: none;
    margin: 14px 0 0;
    padding: 0;
    font-size: 13px;
    line-height: 19px;
    color: var(--ink);
  }
  .contact__list li { display: flex; justify-content: flex-end; align-items: center; gap: 7px; }
  .contact__list svg { position: static; width: 11px; height: 11px; }

  .mark {
    position: absolute;
    left: 62px;
    top: 112px;
    width: 190px;
    height: 150px;
    display: flex;
    align-items: center;
    justify-content: center;
    color: var(--paper);
    font-weight: 300;
    font-size: 22px;
    letter-spacing: 1px;
  }

  .brand__name {
    position: absolute;
    left: 0;
    right: 0;
    top: 92px;
    text-align: center;
    color: var(--paper);
    font-weight: 300;
    font-size: 56px;
    letter-spacing: 2px;
    margin: 0;
  }
  .brand__legal {
    position: absolute;
    right: 66px;
    top: 196px;
    text-align: center;
    color: var(--soft-white);
    font-size: 13px;
    line-height: 19px;
    margin: 0;
    letter-spacing: 0.3px;
  }
</style>
</head>
<body>
<main class="canvas">

  <section class="card card--details" aria-label="Card back with contact details">
    <svg width="540" height="309" viewBox="0 0 540 309" aria-hidden="true">
      <defs>
        <radialGradient id="disc-gloss" cx="0.55" cy="0.25" r="0.7">
          <stop offset="0" stop-color="#3a3a3a"/>
          <stop offset="0.5" stop-color="#111"/>
          <stop offset="1" stop-color="#000"/>
        </radialGradient>
      </defs>
      <circle class="disc-ring" cx="100" cy="330" r="259" fill="none" stroke="#0a0a0a" stroke-width="2"/>
      <circle class="disc" cx="100" cy="330" r="250" fill="url(#disc-gloss)"/>
      <ellipse class="mark-ring" cx="157" cy="187" rx="94" ry="76" fill="none" stroke="#ffffff" stroke-width="2.5"/>
    </svg>

    <div class="mark">Varno Gems</div>

    <div class="contact">
      <p class="contact__name">Corinne Mabbutt</p>
      <p class="contact__title">Gemmologist FGAA</p>
      <p class="contact__city">Perth Australia</p>
      <ul class="contact__list">
        <li>+61 427 806 193
          <svg viewBox="0 0 12 12"><rect x="3" y="0.8" width="6" height="10.4" rx="1.2" fill="none" stroke="#1b1b1b" stroke-width="1.2"/><circle cx="6" cy="9.3" r="0.7" fill="#1b1b1b"/></svg>
        </li>
        <li>corinne@varnogems.com.au
          <svg viewBox="0 0 12 12"><rect x="1" y="2.5" width="10" height="7" rx="1" fill="none" stroke="#1b1b1b" stroke-width="1.2"/><path d="M1.5 3 6 6.6 10.5 3" fill="none" stroke="#1b1b1b" stroke-width="1.1"/></svg>
        </li>
        <li>www.varnogems.com.au
          <svg viewBox="0 0 12 12"><circle cx="6" cy="6" r="5" fill="none" stroke="#1b1b1b" stroke-width="1.1"/><ellipse cx="6" cy="6" rx="2.2" ry="5" fill="none" stroke="#1b1b1b" stroke-width="0.9"/><path d="M1 6h10" stroke="#1b1b1b" stroke-width="0.9"/></svg>
        </li>
      </ul>
    </div>
  </section>

  <section class="card card--brand" aria-label="Card front with business name">
    <svg width="540" height="309" viewBox="0 0 540 309" aria-hidden="true">
      <defs>
        <linearGradient id="brand-gloss" x1="0" y1="0" x2="1" y2="1">
          <stop offset="0" stop-color="#050505"/>
          <stop offset="0.45" stop-color="#2a2a2a"/>
          <stop offset="0.7" stop-color="#0d0d0d"/>
          <stop offset="1" stop-color="#000"/>
        </linearGradient>
      </defs>
      <rect width="540" height="309" fill="url(#brand-gloss)"/>
    </svg>
    <p class="brand__name">Varno Gems</p>
    <p class="brand__legal">Varno Orbix PTY T/AS Varno Gems<br>ABN 72 384 516 907</p>
  </section>

</main>
</body>
</html>
```